" Nós somos uma empresa que realiza monitoramento de solos e lavouras por meio de um sensor de proximidade de solo e sensores de imagens acoplados a drones. Fornecemos mapas nutricionais, de saúde, pragas e infestações para agricultores utilizarem os recursos de agricultura de precisao. "

```html
<!DOCTYPE html>
<html lang="pt-BR">
<head>
<meta charset="UTF-8">
<title>CampoSense Agro — Envelope e Papel Timbrado</title>
<link href="https://fonts.googleapis.com/css2?family=Montserrat:wght@300;400&display=swap" rel="stylesheet">
<style>
  :root {
    --backdrop: #e6e6e4;
    --green: #1d6e2c;
    --green-deep: #145220;
    --green-light: #3f9a3c;
    --yellow: #f3c614;
    --blue: #27318a;
    --paper: #ffffff;
    --ink: #6d6d6d;
  }
  * { margin: 0; padding: 0; box-sizing: border-box; }
  html, body { width: 1200px; height: 1200px; overflow: hidden; }
  body {
    background: var(--backdrop);
    font-family: 'Montserrat', sans-serif;
    position: relative;
  }
  .envelope {
    position: absolute; left: 43px; top: 216px; width: 533px; height: 768px;
    background: radial-gradient(ellipse at 40% 35%, var(--green) 0%, var(--green) 55%, var(--green-deep) 100%);
    overflow: hidden;
  }
  .envelope__flap { position: absolute; left: 0; top: 0; width: 533px; height: 80px; }
  .envelope__emblem {
    position: absolute; left: -60px; top: 140px; width: 360px; height: 360px;
    border-radius: 50%; background: rgba(255,255,255,0.06);
  }
  .envelope__contacts {
    position: absolute; left: 36px; right: 30px; top: 690px;
    display: flex; justify-content: space-between; align-items: center;
    color: #ffffff; font-size: 8px; font-weight: 400; line-height: 1.3;
  }
  .contact { display: flex; align-items: center; gap: 6px; }
  .contact svg { flex: none; }
  .rule { position: absolute; left: 0; right: 0; height: 3px; }
  .envelope .rule--one { top: 735px; background: var(--green-light); }
  .envelope .rule--two { top: 744px; height: 2px; background: var(--green-light); opacity: .7; }

  .letterhead {
    position: absolute; left: 614px; top: 216px; width: 538px; height: 768px;
    background: var(--paper);
    overflow: hidden;
  }
  .brand {
    position: absolute; left: 0; right: 0; top: 380px;
    display: flex; flex-direction: column; align-items: center; gap: 70px;
  }
  .brand__dot { width: 150px; height: 150px; border-radius: 50%; background: var(--green); }
  .brand__name {
    font-size: 28px; font-weight: 300; letter-spacing: 2px; color: var(--ink);
  }
  .brand-mini {
    position: absolute; right: 20px; top: 680px;
    display: flex; align-items: center; gap: 5px;
    font-size: 8px; font-weight: 300; color: var(--ink); letter-spacing: .5px;
  }
  .brand-mini__dot { width: 16px; height: 16px; border-radius: 50%; background: var(--green); }
  .letterhead .rule--one { top: 740px; height: 4px; background: var(--green); }
  .letterhead .rule--two { top: 750px; height: 2px; background: var(--green-light); }
</style>
</head>
<body>
  <section class="envelope">
    <svg class="envelope__flap" viewBox="0 0 533 80" aria-hidden="true">
      <path d="M0 0 H533 V20 Q533 60 505 66 L40 66 Q0 60 0 20 Z" fill="var(--yellow)"/>
    </svg>
    <div class="envelope__emblem"></div>
    <div class="envelope__contacts">
      <div class="contact">
        <svg width="14" height="14" viewBox="0 0 14 14"><circle cx="7" cy="7" r="6.3" fill="none" stroke="#fff" stroke-width="1"/><path d="M4.6 4 l1.4 0 .5 1.6 -.8.6 q.7 1.4 2.1 2.1 l.6-.8 1.6.5 0 1.4 q-4.9 .2 -5.4 -5.4z" fill="#fff"/></svg>
        <span>(21) 90000-4512</span>
      </div>
      <div class="contact">
        <svg width="14" height="14" viewBox="0 0 14 14"><circle cx="7" cy="7" r="6.3" fill="none" stroke="#fff" stroke-width="1"/><path d="M7 3.3 a2.3 2.3 0 0 1 2.3 2.3 c0 1.7 -2.3 4.6 -2.3 4.6 s-2.3-2.9-2.3-4.6 a2.3 2.3 0 0 1 2.3-2.3z" fill="#fff"/><circle cx="7" cy="5.6" r=".8" fill="var(--green)"/></svg>
        <span>Rua das Lavouras 210,<br>Vale Verde - RJ</span>
      </div>
      <div class="contact">
        <svg width="14" height="14" viewBox="0 0 14 14"><circle cx="7" cy="7" r="6.3" fill="none" stroke="#fff" stroke-width="1"/><rect x="3.8" y="4.8" width="6.4" height="4.4" fill="none" stroke="#fff" stroke-width=".9"/><path d="M3.8 4.8 L7 7.4 L10.2 4.8" fill="none" stroke="#fff" stroke-width=".9"/></svg>
        <span>contato@camposense.com</span>
      </div>
    </div>
    <div class="rule rule--one"></div>
    <div class="rule rule--two"></div>
  </section>

  <section class="letterhead">
    <div class="brand">
      <div class="brand__dot"></div>
      <div class="brand__name">CAMPOSENSE AGRO</div>
    </div>
    <div class="brand-mini">
      <span class="brand-mini__dot"></span>
      <span>CAMPOSENSE AGRO</span>
    </div>
    <div class="rule rule--one"></div>
    <div class="rule rule--two"></div>
  </section>
</body>
</html>
```